Website Q48 coffee

I am opening a small business selling locally roasted coffee online. To start with I want a site with three pages. 1. A welcome page with logo and mission/vision. 2. Shopping/ordering page. 3. About Us page. The brand is "Q48 Coffee - Brewed with bright hearts". We are giving back to the downs syndrome community by employing people with down syndrome (Trisomy 21) and buy donating to down syndrome research.

Target Market(s)

Families and friends of people with downs syndrome

Coding

Coded - Design and coding required

Number of Pages Required

3 page

```html
<!DOCTYPE html>
<html lang="en">
<head>
<meta charset="utf-8">
<title>Q48 Coffee – Home</title>
<link href="https://fonts.googleapis.com/css2?family=Mulish:wght@400;500;600&family=Roboto+Condensed:wght@400;500&display=swap" rel="stylesheet">
<style>
  :root{
    --ink:#141414;
    --text:#3a3a3a;
    --white:#ffffff;
    --beige:#f3ebe1;
    --accent:#b58a66;
    --hero-a:#1d2a1a;
    --hero-b:#4a2a1c;
    --band-a:#2a2119;
    --band-b:#5a3d28;
  }
  *{margin:0;padding:0;box-sizing:border-box}
  html,body{width:708px;height:1200px;overflow:hidden;background:var(--white)}
  body{position:relative;font-family:'Mulish',sans-serif;color:var(--text)}
  .abs{position:absolute}

  /* brand */
  .brand{position:absolute;font-family:'Mulish',sans-serif;font-weight:500;color:var(--ink);display:flex;align-items:center;gap:6px;letter-spacing:.5px;white-space:nowrap}
  .brand-mark{width:10px;height:10px;background:var(--ink)}
  .header-brand{left:112px;top:18px;font-size:20px;line-height:24px}
  .footer-brand{left:113px;top:1140px;font-size:16px;line-height:20px}
  .footer-brand .brand-mark{width:8px;height:8px}

  /* nav */
  .nav{font-size:7.5px;color:var(--ink)}
  .nav a{color:inherit;text-decoration:none;position:absolute;white-space:nowrap}
  .nav .active{font-weight:600}
  .header-nav .active{border-bottom:0.8px solid var(--ink);padding-bottom:3px}
  .cart-icon{left:543px;top:22px;width:16px;height:16px;background:var(--accent)}

  /* hero */
  .hero{left:0;top:56px;width:708px;height:292px;background:linear-gradient(120deg,var(--hero-a) 0%,#2c2a1c 45%,var(--hero-b) 100%)}
  .hero-title{left:0;width:708px;top:158px;text-align:center;font-family:'Roboto Condensed',sans-serif;font-weight:400;font-size:23.5px;color:var(--white)}
  .hero-sub{left:0;width:708px;top:191px;text-align:center;font-family:'Roboto Condensed',sans-serif;font-size:15px;color:var(--white)}
  .btn{background:var(--white);color:var(--ink);font-size:9.5px;text-align:center;line-height:18px;width:58px;height:18px}

  /* welcome */
  .leaf-deco{left:0;top:398px;width:150px;height:168px;background:radial-gradient(ellipse at 60% 50%,#f1ebe4 0%,rgba(241,235,228,0) 70%)}
  .bean-deco{left:435px;top:348px;width:273px;height:188px;background:radial-gradient(ellipse at 55% 50%,#f5f3f1 0%,rgba(245,243,241,0) 70%)}
  .cup{left:114px;top:398px;width:144px;height:144px;border-radius:50%;background:radial-gradient(circle at 48% 50%,#c9ab86 0%,#e9ddcd 26%,#f6f6f6 30%,#f2f2f2 70%,#ececec 100%)}
  h2{font-weight:500;color:var(--ink)}
  .welcome-title{left:318px;top:408px;font-size:21px}
  .para{font-size:8px;line-height:15px;color:var(--text)}
  .welcome-copy{left:318px;top:440px;width:285px}
  .read-more{left:318px;top:512px;font-size:10px;color:var(--ink);border-bottom:0.8px solid var(--ink);padding-bottom:1px}

  /* vision & mission */
  .vision-title{left:112px;top:590px;font-size:20px}
  .vision-copy{left:112px;top:621px;width:215px}
  .mission-title{left:113px;top:679px;font-size:20px}
  .mission-copy{left:112px;top:710px;width:228px}
  .team-photo{left:351px;top:589px;width:246px;height:213px;background:linear-gradient(135deg,#e8e6e0 0%,#c9b59a 50%,#6a6660 100%)}

  /* giving band */
  .giving{left:0;top:850px;width:708px;height:265px;background:radial-gradient(ellipse at 50% 50%,var(--band-b) 0%,var(--band-a) 75%)}
  .giving-text{left:60px;width:588px;top:933px;text-align:center;font-size:13.5px;line-height:24px;color:var(--white)}

  /* footer */
  .site-footer{left:0;top:1115px;width:708px;height:85px;background:var(--beige)}
  .copyright{left:114px;top:1170px;font-size:7.5px;color:var(--ink)}
  .contact{font-size:7.5px;line-height:10px;color:var(--ink)}
</style>
</head>
<body>

<header class="site-header">
  <div class="brand header-brand"><span class="brand-mark"></span>Q48 Coffee</div>
  <nav class="nav header-nav">
    <a class="active" style="left:361px;top:25px">Home</a>
    <a style="left:403px;top:25px">Shop Our Products</a>
    <a style="left:490px;top:25px">About Us</a>
    <div class="abs cart-icon">
      <svg width="16" height="16" viewBox="0 0 16 16"><path d="M3 4h1.5l1.5 6h6l1-4H5" fill="none" stroke="#fff" stroke-width="1"/><circle cx="6.5" cy="12" r="0.9" fill="#fff"/><circle cx="11" cy="12" r="0.9" fill="#fff"/></svg>
    </div>
    <a style="left:563px;top:26px">Cart (0)</a>
  </nav>
</header>

<section>
  <div class="abs hero" role="img" aria-label="Photo of two children playing outdoors, one in a wheelchair holding a toy plane"></div>
  <h1 class="abs hero-title">We are a Boutique Coffee Roaster in Australia</h1>
  <p class="abs hero-sub">Supporting The Down Syndrome Research.</p>
  <div class="abs btn" style="left:325px;top:217px">Shop Now</div>
</section>

<section>
  <div class="abs leaf-deco" role="img" aria-label="Faint line illustration of coffee leaves and cherries"></div>
  <div class="abs bean-deco" role="img" aria-label="Faint line illustration of coffee beans"></div>
  <div class="abs cup" role="img" aria-label="Top view of a latte with heart art on a white saucer"></div>
  <h2 class="abs welcome-title">Welcome to Q48 Coffee</h2>
  <p class="abs para welcome-copy">Lorem ipsum dolor sit amet, consectetuer adipiscing elit, sed diam nonummy nibh euismod tincidunt ut laoreet dolore magna aliquam erat volutpat. Ut wisi enim ad minim veniam, quis nostrud exerci tation ullamcorper suscipit lobortis nisl ut aliquip ex ea commodo consequat.</p>
  <a class="abs read-more">Read More About Us</a>
</section>

<section>
  <h2 class="abs vision-title">Our Vision</h2>
  <p class="abs para vision-copy">Develop a company that markets coffee and related products to family and friends of the down syndrome community</p>
  <h2 class="abs mission-title">Our Mission</h2>
  <p class="abs para mission-copy">Create and grow an online company selling contract roasted coffee. As growth permits become a fully vertically integrated coffee company from roasting to our own coffee shop. The company will give significant funds to medical research in downs syndrome and we will hire as many people with Downs syndrome as possible.</p>
  <div class="abs team-photo" role="img" aria-label="Photo of two smiling colleagues standing with arms crossed in a bright office"></div>
</section>

<section>
  <div class="abs giving" role="img" aria-label="Photo of hands holding cups of latte art coffee, darkened"></div>
  <p class="abs giving-text">We Are Giving Back To The Downs Syndrome Community By Employing<br>People With Down Syndrome (Trisomy 21) And Buy Donating To<br>Down Syndrome Research.</p>
  <div class="abs btn" style="left:325px;top:1013px">Shop Now</div>
</section>

<footer>
  <div class="abs site-footer"></div>
  <div class="brand footer-brand"><span class="brand-mark"></span>Q48 Coffee</div>
  <p class="abs copyright">© 2021 Q48 Coffee. All Rights Reserved.</p>
  <nav class="nav footer-nav">
    <a class="active" style="left:366px;top:1138px">Home</a>
    <a style="left:413px;top:1138px">Shop Our Products</a>
    <a style="left:504px;top:1138px">About Us</a>
  </nav>
  <svg class="abs" style="left:366px;top:1163px" width="13" height="13" viewBox="0 0 13 13"><path d="M3 1.5l2 2.5-1 1.2c.8 1.6 2 2.8 3.6 3.6l1.2-1 2.5 2-1.2 1.6C6 11 2 7 1.5 2.7z" fill="none" stroke="#141414" stroke-width=".8"/></svg>
  <div class="abs contact" style="left:385px;top:1165px">Call Us<br>+1 (555) 204-3816</div>
  <svg class="abs" style="left:491px;top:1163px" width="13" height="13" viewBox="0 0 13 13"><rect x="1" y="4" width="11" height="8" fill="none" stroke="#141414" stroke-width=".8"/><path d="M1 4l5.5 4.5L12 4M1 4l5.5-3L12 4" fill="none" stroke="#141414" stroke-width=".8"/></svg>
  <div class="abs contact" style="left:509px;top:1165px">Email<br>hello@q48coffee.com</div>
</footer>

</body>
</html>
```